Donations Website - Fund page design

We need an on brand fund page for our crowdfunding website. The design should keep in mind Quillmark Framegrid 3 default columns and spacing.

Please use this development site as a guide... ( under construction )
http://lenor.pursivo-example.com:8080/

Elements to include:
• Framegrid 3 default column layout ( based on 12 column / 1140px / 30px gutters )
• Fund title ( Default Page Fund Title )
• Fund image / video ( 16:9 ratio )
• Fund progress: Current $ amount, Goal $ amount, # donations, # supporters, # views, % progress, progress bar, # shares
• Share buttons ( Chatterloop, Murmurly, Zentrix+, WorkNestle, Snapboardly, Email )
• Donate button
• Sections for ( Fund story, fund updates and fund comments... could be tabbed )
• Section for recent donations (name + cl photo / icon + anonymous / donation amount, short message )
• Button to report this fund
• Fund created by section ( name, chatterloop photo if they've verified using chatterloop and number of friends )
• Contact fund raiser button/link
Updates

The design brief has been updated. I've attached the logo as well, please use unless you feel you have something better to include.

Thanks.

I can't stress enough that this is 'NOT' a home page design. This is a personal fund page for a single user. Please do not include 'Other funds' on this page to promote.

Thanks,

Edvin

The page should be similar to these pages. As you can see, these are single fund pages within these sites. I do not want my page to look like these, but have the features I included in the brief while fitting my site's design.

http://www.pledgora-example.com/4qa8rb
https://www.launchvane-example.com/projects/502719846/lumo-crest?ref=home_location
http://www.fundquarry-example.com/projects/the-amber-harborfolk

Thanks,

Edvin

Target Market(s)

Adults age 18-50 mainly. Anyone that potentially needs to raise money.

Industry/Entity Type

Construction

Font styles to use
Sans Serif

Colors

Designer to choose colors to be used in the design.

Requirements
Must have
• • Framegrid 3 default column layout ( based on 12 column / 1140px / 30px gutters )
• Donate button
Nice to have
• Would be nice to keep in mind that users may be able to choose a theme color during fund setup. But if the design is strong enough on its own we will not include this option.

```html
<!DOCTYPE html>
<html lang="en">
<head>
<meta charset="utf-8">
<title>First trip to Europe Honeymoon :) — Giftaloft</title>
<link rel="stylesheet" href="https://fonts.googleapis.com/css2?family=Nunito+Sans:ital,wght@0,400;0,600;0,700;0,800;1,400&family=Gelasio:ital@1&display=swap">
<style>
  :root {
    --top-rule: #1b9ad6;
    --brand-green: #2f6c45;
    --brand-green-dark: #285c3b;
    --brand-green-deep: #1f4a2f;
    --accent-orange: #f28a1a;
    --action-blue: #1da0e2;
    --action-red: #e0281e;
    --ink: #2b2b2b;
    --ink-soft: #555;
    --ink-muted: #999;
    --line: #dcdcdc;
    --panel: #f4f4f4;
    --footer: #ebebeb;
    --loop-blue: #3b5998;
    --white: #fff;
  }
  * { box-sizing: border-box; margin: 0; padding: 0; }
  a { text-decoration: none; }
  html, body { width: 1200px; height: 2225px; overflow: hidden; background: var(--white); }
  body { font-family: "Nunito Sans", Arial, sans-serif; color: var(--ink); }
  .page { position: relative; width: 1200px; height: 2225px; overflow: hidden; }

  /* Header */
  .site-header { position: absolute; top: 0; left: 0; width: 1200px; height: 85px; border-top: 4px solid var(--top-rule); background: linear-gradient(#fff, #f3f3f3); border-bottom: 1px solid #ddd; }
  .brand { position: absolute; left: 93px; top: 24px; display: flex; align-items: center; gap: 8px; font-weight: 800; font-size: 23px; letter-spacing: 1px; color: var(--brand-green); }
  .brand-dot { width: 26px; height: 26px; border-radius: 50%; background: var(--brand-green); }
  .main-nav { position: absolute; left: 323px; top: 20px; display: flex; align-items: center; font-size: 12px; font-weight: 700; color: #666; text-transform: uppercase; }
  .main-nav a { color: inherit; padding: 0 14px; border-right: 1px solid #ddd; line-height: 16px; }
  .main-nav a:last-child { border-right: 0; }
  .main-nav .is-current { border: 1px solid #ccc; border-radius: 2px; background: #fff; color: #333; padding: 10px 16px; margin-right: 10px; }
  .header-actions { position: absolute; right: 94px; top: 18px; display: flex; gap: 9px; }
  .btn { display: inline-flex; align-items: center; justify-content: center; color: #fff; font-weight: 700; border-radius: 2px; }
  .btn-signin { width: 91px; height: 39px; background: var(--action-blue); font-size: 15px; }
  .btn-create { width: 209px; height: 39px; background: var(--action-red); font-size: 15px; }

  /* Hero */
  .hero { position: absolute; top: 85px; left: 0; width: 1200px; height: 526px; background: linear-gradient(180deg, #7e5d86 0%, #a0708e 35%, #c98595 65%, #d99a80 100%); }
  .fund-title { position: absolute; left: 93px; top: 36px; font-size: 45px; font-weight: 800; color: #fff; letter-spacing: -0.3px; }
  .fund-media { position: absolute; left: 93px; top: 100px; width: 690px; height: 382px; background: linear-gradient(160deg, #8fa7bd 0%, #b9b3a6 45%, #d8c4a2 70%, #c7a98a 100%); }
  .play-button { position: absolute; left: 311px; top: 133px; width: 68px; height: 68px; }
  .media-strip { position: absolute; left: 0; bottom: 0; width: 100%; height: 33px; background: rgba(40, 30, 40, .55); display: flex; justify-content: center; align-items: center; gap: 6px; }
  .dot { width: 11px; height: 11px; border-radius: 50%; border: 1px solid #bbb; background: transparent; }
  .dot.is-active { background: var(--accent-orange); border-color: var(--accent-orange); }
  .stat-panel { position: absolute; left: 808px; top: 100px; width: 298px; height: 278px; background: rgba(245, 245, 245, .93); border-radius: 2px; }
  .raised { position: absolute; left: 27px; top: 26px; font-size: 45px; font-weight: 800; color: #333; letter-spacing: -0.5px; }
  .progress { position: absolute; left: 27px; top: 80px; width: 248px; height: 12px; background: var(--brand-green-dark); border-radius: 6px; overflow: hidden; }
  .progress-fill { width: 67%; height: 100%; background: #2ea23c; }
  .progress-note { position: absolute; left: 27px; top: 100px; font-size: 12px; color: #555; }
  .panel-rule { position: absolute; left: 27px; top: 128px; width: 248px; border-top: 1px solid #d3d3d3; }
  .stat { position: absolute; top: 141px; }
  .stat-value { display: block; font-size: 33px; font-weight: 800; color: #333; line-height: 38px; }
  .stat-label { display: block; font-size: 13px; color: #666; }
  .stat-supporters { left: 27px; }
  .stat-views { left: 135px; border-left: 1px solid #d3d3d3; padding-left: 14px; }
  .stat-days { left: 207px; border-left: 1px solid #d3d3d3; padding-left: 18px; }
  .ends { position: absolute; left: 27px; top: 220px; font-size: 12px; color: #555; }
  .donate-button { position: absolute; left: 808px; top: 385px; width: 298px; height: 61px; background: var(--accent-orange); color: #fff; font-size: 19px; font-weight: 800; display: flex; align-items: center; justify-content: center; gap: 14px; text-transform: uppercase; border-radius: 2px; }
  .donate-icon { width: 32px; height: 32px; }
  .supporter-note { position: absolute; left: 808px; top: 446px; width: 298px; height: 36px; background: rgba(60, 40, 70, .35); color: #eee; font-size: 12px; display: flex; align-items: center; justify-content: center; }
  .supporter-note a { color: var(--accent-orange); margin-left: 4px; }

  /* Share bar */
  .share-bar { position: absolute; top: 611px; left: 0; width: 1200px; height: 64px; background: linear-gradient(#fafafa, #ececec); border-bottom: 1px solid #ddd; }
  .share-label { position: absolute; left: 93px; top: 22px; font-size: 14px; font-weight: 600; color: #444; }
  .share-item { position: absolute; top: 0; height: 64px; display: flex; align-items: center; justify-content: center; border-left: 1px solid #ddd; font-size: 13px; color: #3a6fb0; gap: 6px; }
  .share-item .mark { width: 11px; height: 11px; border-radius: 2px; }
  .share-count-btn { background: var(--brand-green); color: #fff; font-size: 12px; font-weight: 700; border-radius: 2px; width: 90px; height: 31px; display: flex; align-items: center; justify-content: center; gap: 8px; }
  .share-count-btn span { background: #fff; color: var(--brand-green); border-radius: 9px; padding: 0 6px; font-size: 11px; }
  .like-btn { background: var(--loop-blue); color: #fff; font-size: 11px; font-weight: 700; padding: 2px 6px; border-radius: 2px; }
  .like-count { border: 1px solid #bbb; background: #fff; color: #666; font-size: 11px; padding: 1px 5px; }
  .more-btn { position: absolute; left: 1029px; top: 18px; width: 73px; height: 29px; border: 1px solid #ccc; background: linear-gradient(#fff, #e8e8e8); font-size: 11px; font-weight: 700; color: #444; display: flex; align-items: center; justify-content: center; gap: 6px; border-radius: 2px; }

  /* Organiser band */
  .organiser { position: absolute; top: 675px; left: 0; width: 1200px; height: 292px; background: var(--brand-green); }
  .organiser::after { content: ""; position: absolute; left: 832px; top: 0; height: 247px; border-left: 1px solid rgba(0,0,0,.15); }
  .organiser-photo { position: absolute; left: 97px; top: 57px; width: 136px; height: 136px; border-radius: 50%; border: 4px solid #6b9a7a; background: linear-gradient(135deg, #8cab86, #c69a6e 60%, #52725e); }
  .loop-badge { position: absolute; width: 14px; height: 14px; border-radius: 50%; background: var(--loop-blue); border: 2px solid #fff; }
  .organiser-photo .loop-badge { right: 6px; bottom: 6px; }
  .organiser-name { position: absolute; left: 254px; top: 52px; font-size: 23px; font-weight: 600; color: #fff; }
  .organiser-quote { position: absolute; left: 254px; top: 82px; width: 525px; font-family: "Gelasio", Georgia, serif; font-style: italic; font-size: 16px; line-height: 22px; color: #b5d3be; }
  .friends-title { position: absolute; left: 863px; top: 65px; font-size: 16px; font-weight: 700; color: #fff; }
  .friends { position: absolute; left: 863px; top: 100px; width: 250px; display: flex; flex-wrap: wrap; gap: 8px 8px; }
  .friend { width: 28px; height: 28px; border-radius: 50%; background: linear-gradient(135deg, #b88a6e, #5c4a3f); }
  .tabs { position: absolute; left: 93px; top: 247px; display: flex; gap: 4px; }
  .tab { height: 45px; display: flex; align-items: center; gap: 9px; padding: 0 22px; background: var(--brand-green-deep); color: #fff; font-size: 16px; font-weight: 700; }
  .tab.is-active { background: var(--accent-orange); }
  .tab svg { width: 15px; height: 15px; }

  /* Main content */
  .content { position: absolute; top: 967px; left: 0; width: 1200px; height: 1164px; }
  .content::before { content: ""; position: absolute; left: 832px; top: 0; bottom: 0; border-left: 1px solid #e4e4e4; }
  .story { position: absolute; left: 93px; top: 58px; width: 705px; }
  .section-title { font-size: 29px; font-weight: 700; color: #222; margin-bottom: 4px; }
  .story p { font-size: 15.6px; line-height: 22px; color: #555; margin-bottom: 22px; letter-spacing: -0.1px; }
  .story a { color: var(--accent-orange); }

  .comments { position: absolute; left: 93px; top: 472px; width: 718px; }
  .comments-sub { font-size: 12px; color: #888; margin-top: -2px; }
  .loop-signin { position: absolute; right: 4px; top: 4px; width: 177px; height: 26px; background: var(--loop-blue); color: #fff; font-size: 10.5px; font-weight: 700; display: flex; align-items: center; justify-content: center; gap: 7px; border-radius: 2px; }
  .loop-signin i { width: 10px; height: 10px; background: #fff; display: block; border-radius: 1px; }
  .email-signin { position: absolute; right: 4px; top: 38px; font-size: 10.5px; color: #888; }
  .comments-rule { border-top: 1px solid #ddd; margin-top: 33px; }
  .comment-list { list-style: none; margin-top: 24px; }
  .comment { position: relative; padding-left: 61px; margin-bottom: 28px; }
  .comment-avatar { position: absolute; left: 0; top: 2px; width: 48px; height: 48px; border-radius: 50%; background: linear-gradient(135deg, #9d7a66, #3f3a3a); }
  .comment-avatar .loop-badge { right: -3px; bottom: -1px; }
  .comment-avatar.is-guest { background: #eef1f2; border: 1px solid #e3e6e8; }
  .comment-card { border: 1px solid #d5d5d5; background: #fff; }
  .comment-body { padding: 13px 14px 14px; }
  .comment-meta { font-size: 11px; color: #aaa; }
  .comment-meta b { color: #333; font-weight: 700; }
  .comment-text { font-family: "Gelasio", Georgia, serif; font-style: italic; font-size: 16px; line-height: 22px; color: #222; margin-top: 6px; }
  .comment-foot { background: #e9ecee; border-top: 1px solid #d5d5d5; height: 25px; padding: 0 12px; display: flex; align-items: center; justify-content: space-between; font-size: 10.5px; color: #888; }
  .comment-foot a { color: #2a8ac4; font-weight: 700; }
  .comment-foot time { font-style: italic; color: #aaa; }

  /* Sidebar */
  .sidebar { position: absolute; left: 860px; top: 58px; width: 246px; }
  .recent { border: 1px solid #ddd; border-radius: 2px; background: #fff; }
  .recent-head { height: 47px; border-bottom: 1px solid #e3e3e3; background: #fafafa; display: flex; align-items: center; justify-content: center; gap: 10px; font-size: 16px; font-weight: 700; color: var(--brand-green-deep); }
  .recent-head svg { width: 16px; height: 16px; }
  .donation-photo { margin: 22px 0 0 20px; width: 206px; height: 118px; background: linear-gradient(135deg, #5c4b42, #8a6f63 45%, #c99f7b 80%, #d9c25e); }
  .donor { position: relative; height: 86px; }
  .donor-avatar { position: absolute; left: 24px; top: 15px; width: 54px; height: 54px; border-radius: 50%; background: linear-gradient(135deg, #b28a72, #4a3a32); }
  .donor-avatar .loop-badge { right: -2px; bottom: 0; }
  .donor-name { position: absolute; left: 88px; top: 24px; font-size: 16.5px; font-weight: 700; color: #222; white-space: nowrap; }
  .donor-amount { position: absolute; left: 88px; top: 46px; font-size: 24px; font-weight: 800; color: var(--accent-orange); }
  .donor-message { margin: 0 22px 0 26px; font-size: 11px; line-height: 17px; color: #555; height: 50px; }
  .recent-foot { height: 37px; border-top: 1px solid #e3e3e3; background: #f6f6f6; display: flex; align-items: center; justify-content: space-between; padding: 0 9px 0 26px; }
  .recent-foot .dots { display: flex; gap: 5px; }
  .more-donations { background: var(--brand-green); color: #fff; font-size: 9px; font-weight: 800; width: 102px; height: 23px; display: flex; align-items: center; justify-content: center; border-radius: 2px; }
  .become-fundraiser { margin-top: 17px; width: 246px; height: 46px; background: var(--action-blue); color: #fff; font-size: 14px; font-weight: 700; display: flex; align-items: center; justify-content: center; border-radius: 2px; }
  .fund-links { margin-top: 18px; border: 1px solid #e0e0e0; border-radius: 2px; list-style: none; }
  .fund-links li { height: 37px; display: flex; align-items: center; gap: 12px; padding-left: 17px; font-size: 13px; color: #555; }
  .fund-links li + li { border-top: 1px solid #e8e8e8; }
  .fund-links svg { width: 14px; height: 14px; }

  /* Footer */
  .site-footer { position: absolute; top: 2131px; left: 0; width: 1200px; height: 94px; background: var(--footer); }
  .footer-links { position: absolute; left: 93px; top: 26px; font-size: 12px; color: #777; }
  .copyright { position: absolute; left: 93px; top: 47px; font-size: 12px; color: #777; }
  .follow { position: absolute; right: 94px; top: 30px; display: flex; align-items: center; gap: 9px; font-size: 12px; color: #777; }
  .follow-links { display: flex; gap: 9px; color: #555; font-weight: 700; }
</style>
</head>
<body>
<div class="page">

  <header class="site-header">
    <div class="brand"><span class="brand-dot"></span>GIFTALOFT</div>
    <nav class="main-nav">
      <a class="is-current" href="#">How it works</a>
      <a href="#">FAQs</a>
      <a href="#">Support</a>
      <a href="#">About</a>
    </nav>
    <div class="header-actions">
      <a class="btn btn-signin" href="#">Sign In</a>
      <a class="btn btn-create" href="#">Create Your Furnraiser</a>
    </div>
  </header>

  <section class="hero">
    <h1 class="fund-title">First trip to Europe Honeymoon:)</h1>
    <div class="fund-media" role="img" aria-label="Video still of the couple sitting together on a sunny beach">
      <svg class="play-button" viewBox="0 0 68 68" aria-hidden="true">
        <circle cx="34" cy="34" r="33" fill="#fff"/>
        <circle cx="34" cy="34" r="26" fill="#e0281e"/>
        <path d="M28 22 L46 34 L28 46 Z" fill="#fff"/>
      </svg>
      <div class="media-strip">
        <span class="dot"></span><span class="dot is-active"></span><span class="dot"></span><span class="dot"></span><span class="dot"></span>
      </div>
    </div>

    <div class="stat-panel">
      <div class="raised">$27,118</div>
      <div class="progress"><div class="progress-fill"></div></div>
      <div class="progress-note">90% raised of $30k goal</div>
      <div class="panel-rule"></div>
      <div class="stat stat-supporters"><span class="stat-value">918</span><span class="stat-label">Supporters</span></div>
      <div class="stat stat-views"><span class="stat-value">241</span><span class="stat-label">Views</span></div>
      <div class="stat stat-days"><span class="stat-value">15</span><span class="stat-label">Days</span></div>
      <div class="ends">Ends Mar 28, 2014 at 11:59PM PST</div>
    </div>

    <a class="donate-button" href="#">
      <svg class="donate-icon" viewBox="0 0 32 32" aria-hidden="true">
        <circle cx="16" cy="16" r="16" fill="#fff"/>
        <path d="M16 24 C9 18 8 15 8 13 C8 10.5 10 9 12 9 C13.8 9 15.2 10 16 11.5 C16.8 10 18.2 9 20 9 C22 9 24 10.5 24 13 C24 15 23 18 16 24 Z" fill="#f28a1a"/>
      </svg>
      Make a Donation
    </a>
    <div class="supporter-note">Not Ready to Donate? <a href="#">Become a Supporter</a></div>
  </section>

  <section class="share-bar">
    <span class="share-label">Share this fund:</span>
    <div class="share-item" style="left:219px;width:110px;"><span class="share-count-btn">Share <span>20</span></span></div>
    <div class="share-item" style="left:329px;width:137px;"><span class="like-btn">Like</span><span class="like-count">2.8k</span></div>
    <div class="share-item" style="left:466px;width:100px;"><i class="mark" style="background:#3b5998"></i>Share</div>
    <div class="share-item" style="left:566px;width:115px;"><i class="mark" style="background:#1da0e2"></i>Tweet</div>
    <div class="share-item" style="left:681px;width:106px;"><i class="mark" style="background:#d8262b"></i>Pin it</div>
    <div class="share-item" style="left:787px;width:112px;"><i class="mark" style="background:#6a8fb8"></i>Email</div>
    <div class="share-item" style="left:899px;width:109px;border-right:1px solid #ddd;"><i class="mark" style="background:#6a8fb8"></i>Embed</div>
    <div class="more-btn">MORE <svg width="7" height="5" viewBox="0 0 7 5" aria-hidden="true"><path d="M0 0 H7 L3.5 5 Z" fill="#444"/></svg></div>
  </section>

  <section class="organiser">
    <div class="organiser-photo" role="img" aria-label="Portrait of the fund organiser outdoors in a sun hat"><span class="loop-badge"></span></div>
    <h2 class="organiser-name">From Marla Quent</h2>
    <p class="organiser-quote">For our plunge into married lifee into married lifee into married life, Teodor and I are attempting the world's deepest underwater wedding on September 30, 2013 For our plunge into married lifee into married life into married life, Teodor and I are attempting the world's deepest under-water wedding...</p>
    <h3 class="friends-title">Friends from Chatterloop</h3>
    <div class="friends" role="img" aria-label="Profile photos of eleven Chatterloop friends">
      <span class="friend"></span><span class="friend"></span><span class="friend"></span><span class="friend"></span><span class="friend"></span><span class="friend"></span><span class="friend"></span>
      <span class="friend"></span><span class="friend"></span><span class="friend"></span><span class="friend"></span>
    </div>
    <nav class="tabs">
      <span class="tab is-active"><svg viewBox="0 0 15 15" aria-hidden="true"><rect x="1" y="2" width="13" height="11" rx="1" fill="#fff"/><path d="M7.5 3 V13" stroke="#f28a1a" stroke-width="1.2"/></svg>Fund story</span>
      <span class="tab"><svg viewBox="0 0 15 15" aria-hidden="true"><circle cx="2.5" cy="12.5" r="1.8" fill="#fff"/><path d="M1 6.5 A7.5 7.5 0 0 1 8.5 14" stroke="#fff" stroke-width="2" fill="none"/><path d="M1 1.5 A12.5 12.5 0 0 1 13.5 14" stroke="#fff" stroke-width="2" fill="none"/></svg>Fund updates</span>
      <span class="tab"><svg viewBox="0 0 15 15" aria-hidden="true"><path d="M1 2 H14 V10 H6 L3 13 V10 H1 Z" fill="#fff"/></svg>Fund comments</span>
    </nav>
  </section>

  <main class="content">
    <article class="story">
      <h2 class="section-title">The Story</h2>
      <p>For our plunge into married life, Teodor and I are attempting the world's deepest underwater wed-ding on September 30, 2013. Six months up to our wedding we have dedicated every ounce of our energy to preparations for our big day when we dive to 123 meters to say "I do." We have been training, purchasing new dive equipment and practicing our skills non-stop.</p>
      <p>With less than 3 months to go, we are asking for support from anyone who would like to help us make the best of our actual wedding day and our future careers as technical dive instructors. There are still essential items of equipment and preparation costs that we are hoping to finance, but they won't be possible without your help!</p>
      <p>For further details and a complete article on our record-breaking wedding attempt, please email me at <a href="#">divewed@mailnook-example.com!</a></p>
      <p>Thanks for your well-wishings and any support you can give!</p>
    </article>

    <section class="comments">
      <h2 class="section-title">Fund Comments</h2>
      <p class="comments-sub">Use your Chatterloop sign in to add a comment.</p>
      <span class="loop-signin"><i></i>SIGN IN WITH CHATTERLOOP</span>
      <span class="email-signin">Sign in with email</span>
      <div class="comments-rule"></div>
      <ol class="comment-list">
        <li class="comment">
          <div class="comment-avatar" role="img" aria-label="Commenter profile photo"><span class="loop-badge"></span></div>
          <div class="comment-card">
            <div class="comment-body">
              <div class="comment-meta"><b>Pia Holloran</b> commented with a support:</div>
              <p class="comment-text">You can do it! Then we can have a tea party!</p>
            </div>
            <div class="comment-foot"><span><a href="#">Like</a> · 1 Like</span><time>2 days ago</time></div>
          </div>
        </li>
        <li class="comment" style="margin-bottom:33px">
          <div class="comment-avatar" role="img" aria-label="Commenter profile photo"><span class="loop-badge"></span></div>
          <div class="comment-card">
            <div class="comment-body">
              <div class="comment-meta"><b>Ines Varrow</b> commented with a support:</div>
              <p class="comment-text">I really like what you do see my company<br>www.stitchery-example.com/crochet</p>
            </div>
            <div class="comment-foot"><span><a href="#">Like</a> · 1 Like</span><time>3 days ago</time></div>
          </div>
        </li>
        <li class="comment">
          <div class="comment-avatar" role="img" aria-label="Commenter profile photo"><span class="loop-badge"></span></div>
          <div class="comment-card">
            <div class="comment-body">
              <div class="comment-meta"><b>Dorian Welke</b> commented with a $25 donation:</div>
              <p class="comment-text">yummy yummy tea mmmm</p>
            </div>
            <div class="comment-foot"><span><a href="#">Like</a> · 1 Like</span><time>4 days ago</time></div>
          </div>
        </li>
        <li class="comment">
          <div class="comment-avatar is-guest" role="img" aria-label="Default guest avatar"></div>
          <div class="comment-card">
            <div class="comment-body">
              <div class="comment-meta"><b>Bea Lindqvar</b> commented with a $10 donation:</div>
              <p class="comment-text">Wish it could be more! Good luck, can't wait to try the<br>tea!!</p>
            </div>
            <div class="comment-foot"><span><a href="#">Like</a> · 1 Like</span><time>2 days ago</time></div>
          </div>
        </li>
      </ol>
    </section>

    <aside class="sidebar">
      <div class="recent">
        <div class="recent-head">
          <svg viewBox="0 0 16 16" aria-hidden="true"><path d="M8 15 V8 M8 8 C8 4 5 2 2 2 C2 6 4 8 8 8 Z M8 8 C8 4 11 2 14 2 C14 6 12 8 8 8 Z" fill="#1f4a2f" stroke="#1f4a2f" stroke-width="1.2"/></svg>
          Recent Donations
        </div>
        <div class="donation-photo" role="img" aria-label="Photo of the donor's family holding a bright woven cloth indoors"></div>
        <div class="donor">
          <div class="donor-avatar" role="img" aria-label="Donor profile photo"><span class="loop-badge"></span></div>
          <div class="donor-name">Odette Brannock</div>
          <div class="donor-amount">$240</div>
        </div>
        <p class="donor-message">Natural teas for a Supernatural life.After 6 years of blending my own teas, 14 yrs teaching.</p>
        <div class="recent-foot">
          <div class="dots"><span class="dot"></span><span class="dot is-active"></span><span class="dot"></span><span class="dot"></span><span class="dot"></span></div>
          <span class="more-donations">MORE DONATIONS</span>
        </div>
      </div>
      <a class="become-fundraiser" href="#">BECOME A FUNDRAISER</a>
      <ul class="fund-links">
        <li><svg viewBox="0 0 14 14" aria-hidden="true"><circle cx="7" cy="7" r="6.5" fill="#aaa"/><rect x="6.2" y="3" width="1.6" height="5" fill="#fff"/><rect x="6.2" y="9.3" width="1.6" height="1.6" fill="#fff"/></svg>Report this fund</li>
        <li><svg viewBox="0 0 14 14" aria-hidden="true"><rect x="1" y="3" width="12" height="8.5" fill="#aaa"/><path d="M1 3 L7 8 L13 3" stroke="#fff" stroke-width="1.2" fill="none"/></svg>Contact fund raiser</li>
      </ul>
    </aside>
  </main>

  <footer class="site-footer">
    <div class="footer-links">Home · Press · FAQ · Blog · Terms · Privacy</div>
    <div class="copyright">© 2014 Pledgehaven-example.com</div>
    <div class="follow">Follow Us On:
      <span class="follow-links"><span>Murmurly</span><span>Chatterloop</span><span>WorkNestle</span><span>Zentrix+</span><span>Snapboardly</span></span>
    </div>
  </footer>

</div>
</body>
</html>
```